Business card design needed

Tallowind Limited is a management company that manages Marrowbay Swift Journeys ticketing agency for Skyreach Carriers and Upper Ridge Pressworks a small printing company in Mt Hagen Papua New Guinea.

Industry/Entity Type

Printing

Contact Information for Business Card

Tallowind Limited
Rosalind Kewatuma
P: +675 318 4457 F: +675 318 4493
Po Box 617 Mt Hagen WHP
Papua New Guinea
E: rosalind@tallowindlimited.example

Logo Text

Tallowind Limited

Logo styles of interest
Emblem Logo
Requirements
Must have
• Bottom Left hand corner of business card to have a small globe with Papua New Guinea in the middle Australia showing at the bottom and Footprints walking from PNG up and spiralling down the globe (like an ANT Trail) than down and walking along the bottom of business card with Marking Every Moment Kindly in the middle of the card. CARD TO BE DONE IN TWO COLORS Black background and Electric Blue writing
Nice to have
• Printing Both sides
on Front as per above details
on Back, all to be Centered

Tallowind Limited
Managing
Marrowbay Swift Journeys
+675 318 4457
Upper Ridge Pressworks
+675 318 5276

```html
<!DOCTYPE html>
<html lang="en">
<head>
<meta charset="utf-8">
<title>Tallowind Limited – Business Card</title>
<link rel="stylesheet" href="https://fonts.googleapis.com/css2?family=Questrial&display=swap">
<style>
  :root {
    --card-black: #231f20;
    --electric-blue: #00aeef;
    --page-bg: #d9d6d2;
    --globe-deep: #2e3a8c;
    --globe-light: #8f9ad6;
    --trail-tint: rgba(255, 255, 255, 0.12);
    --faint-mark: rgba(255, 255, 255, 0.05);
    --band-text: #ffffff;
  }
  * { box-sizing: border-box; margin: 0; padding: 0; }
  html, body {
    width: 1200px;
    height: 1000px;
    overflow: hidden;
    background: var(--page-bg);
    font-family: "Questrial", "Century Gothic", sans-serif;
  }
  .card {
    position: absolute;
    left: 165px;
    width: 870px;
    height: 430px;
    background: var(--card-black);
    border-radius: 30px;
    overflow: hidden;
    color: var(--electric-blue);
  }
  .card--back { top: 40px; }
  .card--front { top: 520px; }

  /* Back side: contact block */
  .faint-mark {
    position: absolute;
    left: 60px;
    top: 70px;
    width: 110px;
    height: 250px;
    background: var(--faint-mark);
    border-radius: 20px;
  }
  .contact {
    position: absolute;
    left: 200px;
    top: 42px;
    width: 460px;
    text-align: center;
    line-height: 1.18;
  }
  .contact__company { font-size: 36px; }
  .contact__name { font-size: 31px; }
  .contact__line { font-size: 26px; }
  .contact__role { font-size: 17px; margin-top: 4px; }

  .info-band {
    position: absolute;
    left: 0;
    right: 0;
    bottom: 52px;
    height: 42px;
    background: var(--electric-blue);
    display: flex;
    align-items: center;
    justify-content: space-between;
    padding: 0 34px;
    color: var(--band-text);
    font-size: 15px;
  }

  /* Front side: emblem */
  .top-rule {
    position: absolute;
    left: 250px;
    right: 0;
    top: 40px;
    height: 5px;
    background: var(--electric-blue);
  }
  .globe {
    position: absolute;
    left: 70px;
    top: 150px;
    width: 185px;
    height: 185px;
    border-radius: 50%;
    background: radial-gradient(circle at 45% 30%, var(--globe-light), var(--globe-deep) 70%);
  }
  .trail {
    position: absolute;
    left: 40px;
    right: 40px;
    bottom: 22px;
    height: 28px;
    border-radius: 14px;
    background: var(--trail-tint);
  }
  .brand-name {
    position: absolute;
    left: 255px;
    top: 140px;
    font-size: 50px;
    color: var(--electric-blue);
  }
</style>
</head>
<body>
  <section class="card card--back" aria-label="Business card, contact side">
    <div class="faint-mark" role="img" aria-label="Faint footprint decoration"></div>
    <div class="contact">
      <p class="contact__company">Tallowind Limited</p>
      <p class="contact__name">Rosalind Kewatuma</p>
      <p class="contact__line">Po Box 617</p>
      <p class="contact__line">Mt Hagen WHP</p>
      <p class="contact__line">Papua New Guinea</p>
      <p class="contact__line">P:&nbsp; +675 318 4457</p>
      <p class="contact__line">F:&nbsp; +675 318 4493</p>
      <p class="contact__line">E: rosalind@tallowindlimited.example</p>
      <p class="contact__role">Tallowind Limited Managing</p>
    </div>
    <div class="info-band">
      <span class="info-band__item">Marrowbay Swift Journeys P:+675 318 4457</span>
      <span class="info-band__item">Upper Ridge Pressworks P:+675 318 5276</span>
    </div>
  </section>

  <section class="card card--front" aria-label="Business card, emblem side">
    <div class="top-rule"></div>
    <div class="trail" role="img" aria-label="Trail of small white footprints walking along the bottom of the card"></div>
    <div class="globe" role="img" aria-label="Globe showing Papua New Guinea with Australia below and footprints walking over it"></div>
    <p class="brand-name">Tallowind Limited</p>
  </section>
</body>
</html>
```